Pebble Lantern Fine Chocolates
Handcrafted in Sandridge, New Mexico
Pebble Lantern Fine Chocolates -
Creative Brief
Customers who buy my chocolates or are interested in knowing more and purchasing them in the future. Foodies, Downtowners, Tucson tourists, students, coffee shop-types, mostly women.
they need to fit in a box that is 6 1/2 inches by 3 7/8 inches. Ideally, they will be approximately 4.5 inches by 13 3/4 inches, and then fold like an accordian 5 times to be 4.5 by 2 3/4 in your hand.

```html
<!DOCTYPE html>
<html lang="en">
<head>
<meta charset="utf-8">
<title>Pebble Lantern Fine Chocolates – Menu Card</title>
<link href="https://fonts.googleapis.com/css2?family=Open+Sans:wght@400;600&display=swap" rel="stylesheet">
<style>
  :root{
    --ink:#0b0303;
    --glow:#7a1a0c;
    --glow-mid:#3a0905;
    --gold:#d9a441;
    --gold-light:#f3d27a;
    --cream:#f4e6c8;
    --orange:#f2962b;
    --mint:#6fd15a;
    --berry:#e0322c;
    --teal:#3fb6c9;
    --body:#e88a3a;
  }
  *{box-sizing:border-box;margin:0;padding:0}
  html,body{width:1200px;height:830px;overflow:hidden;background:#fff}
  body{font-family:"Open Sans",sans-serif;position:relative}
  .sheet{position:absolute;inset:0;display:grid;grid-template-columns:repeat(5,235px);
    grid-template-rows:390px 390px;column-gap:6px;row-gap:50px}
  .panel{position:relative;overflow:hidden;
    background:radial-gradient(ellipse 75% 55% at 50% 42%,var(--glow) 0%,var(--glow-mid) 50%,var(--ink) 100%)}
  .panel--back{background:#000}
  .frame{position:absolute;inset:0;width:100%;height:100%}
  .brand{position:absolute;top:22px;left:0;right:0;text-align:center;color:var(--gold-light);
    font-size:9px;font-weight:600;letter-spacing:.3px}
  .flavor{position:absolute;top:84px;left:30px;right:30px;text-align:center;font-size:19px;font-weight:400;line-height:1.1;color:var(--cream)}
  .flavor small{display:block;font-size:15px}
  .flavor--orange{color:var(--orange)}
  .flavor--mint{color:var(--mint)}
  .flavor--berry{color:var(--berry)}
  .flavor--teal{color:var(--teal)}
  .flavor--cream{color:var(--cream)}
  .flavor--cream small{color:var(--orange);font-size:19px}
  .blurb{position:absolute;top:150px;left:40px;right:40px;text-align:center;font-size:6.3px;line-height:1.45;color:var(--body)}
  .blurb--low{top:172px}
  .truffle{position:absolute;left:80px;top:293px;width:76px;height:76px;border-radius:50%;
    background:radial-gradient(circle at 45% 40%,#c86a3a 0%,#6b2a14 45%,#cfcfd4 70%,#6a6a70 100%);
    box-shadow:0 0 0 2px var(--gold)}
  .heart-rays{position:absolute;left:20px;top:90px;width:195px;height:170px;
    background:radial-gradient(ellipse at 50% 45%,#d8782e 0%,#8a2e10 40%,transparent 75%)}
  .heart-brand{position:absolute;top:220px;left:0;right:0;text-align:center;color:var(--gold-light);font-size:11px;font-weight:600;line-height:1.3}
  .heart-brand span{display:block;font-size:6.5px;color:var(--orange);letter-spacing:1px}
  .back-brand{position:absolute;top:42px;left:0;right:0;text-align:center;color:var(--gold-light);font-size:11px;font-weight:600;line-height:1.4}
  .back-brand span{display:block;font-size:6px;color:var(--cream);letter-spacing:1px}
  .blossom{position:absolute;left:62px;top:150px;width:112px;height:150px;border-radius:50% 50% 40% 40%;
    background:radial-gradient(circle at 55% 30%,#f1cf45 0%,#c99a22 35%,#5c6a1c 70%,transparent 72%)}
  .back-mark{position:absolute;top:312px;left:0;right:0;text-align:center;color:var(--gold-light);font-size:7px;font-weight:600}
  .origin{position:absolute;top:342px;left:0;right:0;text-align:center;color:var(--cream);font-size:6.5px}
  .contact{position:absolute;top:356px;left:0;right:0;text-align:center;color:#9a8a70;font-size:5px;line-height:1.5}
</style>
</head>
<body>
<svg width="0" height="0" style="position:absolute" aria-hidden="true">
  <defs>
    <linearGradient id="goldLine" x1="0" y1="0" x2="1" y2="1">
      <stop offset="0" stop-color="#f6dc8c"/><stop offset=".5" stop-color="#b9822a"/><stop offset="1" stop-color="#f0c86a"/>
    </linearGradient>
    <path id="labelShape" d="M82,12 H153 Q160,12 160,22 V36 Q160,60 199,68 Q208,70 208,80 V325 Q208,372 168,378 H67 Q27,372 27,325 V80 Q27,70 36,68 Q75,60 75,36 V22 Q75,12 82,12 Z"/>
  </defs>
</svg>

<main class="sheet">
  <section class="panel">
    <svg class="frame" viewBox="0 0 235 390"><use href="#labelShape" fill="none" stroke="url(#goldLine)" stroke-width="3"/></svg>
    <div class="brand">Pebble Lantern</div>
    <h2 class="flavor flavor--cream">Dark Chocolate<small>Caramels</small></h2>
    <p class="blurb blurb--low">Buttery caramel cooked slowly with a pinch of sea salt, wrapped in a rich dark chocolate shell for a smooth, lingering finish.</p>
    <div class="truffle" role="img" aria-label="Photo of a dark chocolate caramel"></div>
  </section>

  <section class="panel">
    <svg class="frame" viewBox="0 0 235 390"><use href="#labelShape" fill="none" stroke="url(#goldLine)" stroke-width="3"/></svg>
    <div class="brand">Pebble Lantern</div>
    <h2 class="flavor flavor--orange">Mexican Toffee</h2>
    <p class="blurb">Crunchy toffee brittle with toasted almonds and a warm hint of cinnamon, coated in dark chocolate and a dusting of spice.</p>
    <div class="truffle" role="img" aria-label="Photo of a Mexican toffee chocolate"></div>
  </section>

  <section class="panel">
    <svg class="frame" viewBox="0 0 235 390"><use href="#labelShape" fill="none" stroke="url(#goldLine)" stroke-width="3"/></svg>
    <div class="brand">Pebble Lantern</div>
    <h2 class="flavor flavor--orange">La Chispa</h2>
    <p class="blurb">A lively truffle of dark ganache, bright orange zest and a touch of chile that leaves a spark at the end of every bite.</p>
    <div class="truffle" role="img" aria-label="Photo of a La Chispa truffle"></div>
  </section>

  <section class="panel">
    <svg class="frame" viewBox="0 0 235 390"><use href="#labelShape" fill="none" stroke="url(#goldLine)" stroke-width="3"/></svg>
    <div class="brand">Pebble Lantern</div>
    <h2 class="flavor flavor--orange">Café Dorado</h2>
    <p class="blurb">Fresh roasted coffee meets golden brown sugar in a silky ganache, finished in dark chocolate for a mellow treat.</p>
    <div class="truffle" role="img" aria-label="Photo of a Café Dorado chocolate"></div>
  </section>

  <section class="panel">
    <div class="heart-rays" role="img" aria-label="Radiating light rays behind the heart"></div>
    <svg class="frame" viewBox="0 0 235 390">
      <rect x="8" y="8" width="219" height="374" fill="none" stroke="url(#goldLine)" stroke-width="2"/>
      <path d="M117,300 C60,250 30,210 30,165 C30,128 60,108 88,112 C104,114 114,124 117,136 C120,124 130,114 146,112 C174,108 205,128 205,165 C205,210 174,250 117,300 Z" fill="#120303" stroke="url(#goldLine)" stroke-width="3"/>
    </svg>
    <div class="heart-brand">Pebble Lantern<span>FINE CHOCOLATES</span></div>
  </section>

  <section class="panel">
    <svg class="frame" viewBox="0 0 235 390"><use href="#labelShape" fill="none" stroke="url(#goldLine)" stroke-width="3"/></svg>
    <div class="brand">Pebble Lantern</div>
    <h2 class="flavor flavor--orange">Horchata</h2>
    <p class="blurb">Creamy white chocolate infused with rice milk, vanilla and cinnamon, inspired by the sweet drink of summer markets.</p>
    <div class="truffle" role="img" aria-label="Photo of a horchata chocolate"></div>
  </section>

  <section class="panel">
    <svg class="frame" viewBox="0 0 235 390"><use href="#labelShape" fill="none" stroke="url(#goldLine)" stroke-width="3"/></svg>
    <div class="brand">Pebble Lantern</div>
    <h2 class="flavor flavor--mint">Vanilla Mint<small>with Lavender</small></h2>
    <p class="blurb blurb--low">Cool garden mint and a whisper of lavender blended into vanilla ganache, dipped in dark chocolate for a calm finish.</p>
    <div class="truffle" role="img" aria-label="Photo of a vanilla mint lavender chocolate"></div>
  </section>

  <section class="panel">
    <svg class="frame" viewBox="0 0 235 390"><use href="#labelShape" fill="none" stroke="url(#goldLine)" stroke-width="3"/></svg>
    <div class="brand">Pebble Lantern</div>
    <h2 class="flavor flavor--berry">Hibiscus<small>and Blueberry</small></h2>
    <p class="blurb blurb--low">Tart hibiscus flowers and ripe blueberries steeped into a bright ganache and sealed in a thin dark chocolate shell.</p>
    <div class="truffle" role="img" aria-label="Photo of a hibiscus blueberry chocolate"></div>
  </section>

  <section class="panel">
    <svg class="frame" viewBox="0 0 235 390"><use href="#labelShape" fill="none" stroke="url(#goldLine)" stroke-width="3"/></svg>
    <div class="brand">Pebble Lantern</div>
    <h2 class="flavor flavor--teal">Tamarind Chile</h2>
    <p class="blurb">Sweet and sour tamarind paired with a gentle chile heat, folded into dark ganache for a bold southwestern bite.</p>
    <div class="truffle" role="img" aria-label="Photo of a tamarind chile chocolate"></div>
  </section>

  <section class="panel panel--back">
    <div class="back-brand">Pebble Lantern<span>FINE CHOCOLATES</span></div>
    <div class="blossom" role="img" aria-label="Illustration of a yellow desert wildflower"></div>
    <div class="back-mark">Pebble Lantern</div>
    <p class="origin">Handcrafted in Sandridge, New Mexico</p>
    <p class="contact">Tel: 505-555-0148<br>pebblelantern.com</p>
  </section>
</main>
</body>
</html>
```